Dental specialist needs a sharp looking letterhead

I am looking for a letterhead to be used to send letters and communication between myself (a dental specialist) and other dentists.
My office is a state of the art dental specialty office.
I need to letterhead to also state:
Gideon R. Whitfield DDS
2847 Birchmont Avenue, Suite K
West Harlow, NY 14391
(716)482-9163
fax: (716)482-9170
whitfieldroot.com (**this email address may change)

i included my logo designs.
thank you

Target Market(s)

dentists

Industry/Entity Type

Communication

Requirements
Must have
• the included logo, whether the vertical or horizontal versions

```html
<!DOCTYPE html>
<html lang="en">
<head>
<meta charset="utf-8">
<title>Harborline Endodontics Letterhead</title>
<link rel="stylesheet" href="https://fonts.googleapis.com/css2?family=Roboto+Slab:wght@400;600&display=swap">
<style>
  :root {
    --backdrop: #e9e9e9;
    --paper: #f4f4f4;
    --band: #050505;
    --ink-light: #ffffff;
    --accent-blue: #3f8fd2;
    --accent-green: #8cc63f;
  }
  * { margin: 0; padding: 0; box-sizing: border-box; }
  html, body {
    width: 1200px;
    height: 968px;
    overflow: hidden;
    background: var(--backdrop);
    font-family: "Roboto Slab", Georgia, serif;
  }
  .letterhead {
    position: absolute;
    left: 290px;
    top: 54px;
    width: 620px;
    height: 860px;
    background: var(--paper);
    box-shadow: 0 2px 6px rgba(0,0,0,0.12);
  }
  .header-band {
    position: relative;
    height: 128px;
    background: var(--band);
    display: flex;
    justify-content: space-between;
    align-items: flex-end;
    padding: 0 26px 18px 28px;
    color: var(--ink-light);
  }
  .header-rule {
    position: absolute;
    left: 0; right: 0; bottom: 0;
    height: 4px;
    background: linear-gradient(to right, var(--accent-blue) 0 50%, var(--accent-green) 50% 100%);
  }
  .practice-name {
    display: flex;
    align-items: center;
    gap: 8px;
    font-size: 17px;
    font-weight: 600;
    letter-spacing: 0.5px;
    line-height: 1.2;
  }
  .practice-mark {
    width: 12px; height: 12px;
    border-radius: 50%;
    background: var(--accent-blue);
    flex: none;
  }
  .contact-block {
    text-align: right;
    font-size: 9.5px;
    line-height: 1.75;
    align-self: center;
    padding-top: 8px;
  }
  .doctor-name {
    font-size: 13px;
    font-weight: 600;
    margin-bottom: 2px;
  }
  .contact-line { display: flex; justify-content: flex-end; align-items: center; gap: 10px; }
  .contact-item { display: inline-flex; align-items: center; gap: 4px; }
  .contact-icon { width: 9px; height: 9px; flex: none; }
</style>
</head>
<body>
  <main class="letterhead">
    <header class="header-band">
      <div class="practice-name">
        <span class="practice-mark"></span>
        <span>Harborline Endodontics P.C.</span>
      </div>
      <div class="contact-block">
        <p class="doctor-name">Gideon R. Whitfield DDS</p>
        <p class="contact-line">
          <span class="contact-item">
            <svg class="contact-icon" viewBox="0 0 10 10" aria-hidden="true"><circle cx="5" cy="5" r="5" fill="#fff"/><path d="M3.2 2.6l1 .9-.5.8a3.5 3.5 0 0 0 2 2l.8-.5.9 1-.7.7C5 7.4 2.6 5 2.5 3.3z" fill="#000"/></svg>
            (716)482-9163
          </span>
          <span class="contact-item">
            <svg class="contact-icon" viewBox="0 0 10 10" aria-hidden="true"><circle cx="5" cy="5" r="5" fill="#fff"/><rect x="3" y="3.5" width="4" height="3.2" fill="#000"/><rect x="3.7" y="2.4" width="2.6" height="1.2" fill="#000"/></svg>
            fax: (716)482-9170
          </span>
        </p>
        <p class="contact-line">
          <span class="contact-item">
            <svg class="contact-icon" viewBox="0 0 10 10" aria-hidden="true"><circle cx="5" cy="5" r="5" fill="#fff"/><rect x="2.5" y="3.2" width="5" height="3.6" fill="none" stroke="#000" stroke-width="0.8"/><path d="M2.5 3.2L5 5.3 7.5 3.2" fill="none" stroke="#000" stroke-width="0.8"/></svg>
            gideon@whitfieldroot.com
          </span>
        </p>
        <p class="contact-line">
          <span class="contact-item">
            <svg class="contact-icon" viewBox="0 0 10 10" aria-hidden="true"><circle cx="5" cy="5" r="5" fill="#fff"/><path d="M5 2a2 2 0 0 1 2 2c0 1.5-2 4-2 4S3 5.5 3 4a2 2 0 0 1 2-2z" fill="#000"/><circle cx="5" cy="4" r="0.7" fill="#fff"/></svg>
            2847 Birchmont Avenue, Suite K, West Harlow, NY 14391
          </span>
        </p>
      </div>
      <span class="header-rule"></span>
    </header>
  </main>
</body>
</html>
```